Business Card Design for Flood Rescue 360 - Property Restoration Professionals

I need a business card designed for Flood Rescue 360. We are a full-service property restoration solution. Providing water, fire, smoke & storm restoration as well as mold remediation and full remodel or reconstruction to homes and businesses across Dallas-Fort Worth, TX.
Target Market(s)
home and business owners with insurance covered property damage from water, fire or storm related damage
Industry/Entity Type
property restoration
Contact Information for Business Card
Martin Kell General Manager Cell: 214-555-0193 Office: 469-555-0148 email: Martin@FloodRescue360.example services: Water, Fire, Mold, Reconstruction Tagline: Urgency for Your Water Emergency!
Look and feel
Each slider illustrates characteristics of the customer's brand and the style your logo design should communicate.

```html
<!DOCTYPE html>
<html lang="en">
<head>
<meta charset="utf-8">
<title>Flood Rescue 360 – Business Card</title>
<link rel="stylesheet" href="https://fonts.googleapis.com/css2?family=Montserrat:wght@400;500;700;800&display=swap">
<style>
  :root {
    --brand-blue: #0bb0e6;
    --brand-blue-deep: #0a9fd1;
    --card-black: #1b1b1c;
    --ink-white: #ffffff;
    --ink-grey: #8a8c8e;
    --backdrop: #d9dadb;
  }
  * { box-sizing: border-box; margin: 0; padding: 0; }
  html, body { width: 1200px; height: 900px; overflow: hidden; }
  body {
    background: var(--backdrop);
    font-family: "Montserrat", sans-serif;
    position: relative;
  }
  .card {
    position: absolute;
    width: 700px;
    height: 400px;
    box-shadow: 0 8px 24px rgba(0,0,0,.25);
    overflow: hidden;
  }
  .card-back {
    left: 80px; top: 35px;
    background: linear-gradient(135deg, var(--brand-blue) 0%, var(--brand-blue-deep) 100%);
  }
  .card-front {
    left: 420px; top: 465px;
    background: var(--card-black);
    color: var(--ink-white);
  }
  .brand {
    position: absolute;
    right: 40px; top: 44px;
    display: flex; align-items: center; gap: 16px;
  }
  .brand-name {
    font-weight: 800;
    font-size: 40px;
    line-height: 1;
    letter-spacing: -0.5px;
    text-transform: uppercase;
    color: var(--brand-blue);
  }
  .brand-dot {
    width: 58px; height: 58px;
    border-radius: 50%;
    background: var(--brand-blue);
  }
  .services {
    position: absolute;
    right: 40px; top: 150px;
    text-align: right;
  }
  .services-title {
    font-weight: 800;
    font-size: 26px;
    color: var(--brand-blue);
    text-transform: uppercase;
    margin-bottom: 6px;
  }
  .services-list { list-style: none; }
  .services-list li {
    font-size: 17px;
    line-height: 27px;
    display: flex; justify-content: flex-end; align-items: center; gap: 8px;
  }
  .services-list li::after {
    content: "";
    width: 9px; height: 9px;
    border-radius: 50%;
    border: 2px solid var(--ink-grey);
  }
  .person {
    position: absolute;
    left: 0; top: 186px;
    padding-left: 44px;
  }
  .person::before {
    content: "";
    position: absolute;
    left: 0; top: 6px;
    width: 14px; height: 68px;
    background: var(--brand-blue);
  }
  .person-name {
    font-weight: 800;
    font-size: 32px;
    color: var(--brand-blue);
    line-height: 1.1;
  }
  .person-title { font-size: 18px; margin-top: 4px; }
  .tagline { font-size: 17px; margin-top: 18px; }
  .contact-list { list-style: none; margin-top: 12px; }
  .contact-list li {
    display: flex; align-items: center; gap: 10px;
    font-size: 16px; line-height: 24px;
  }
  .contact-list svg { width: 15px; height: 15px; fill: var(--brand-blue); flex: none; }
</style>
</head>
<body>
  <div class="card card-back" role="img" aria-label="Repeating embossed brand-mark pattern on blue"></div>

  <section class="card card-front">
    <div class="brand">
      <span class="brand-name">Flood Rescue 360</span>
      <span class="brand-dot"></span>
    </div>

    <div class="services">
      <h2 class="services-title">Services</h2>
      <ul class="services-list">
        <li>Water</li>
        <li>Fire</li>
        <li>Mold</li>
        <li>Reconstruction</li>
      </ul>
    </div>

    <div class="person">
      <h1 class="person-name">Martin Kell</h1>
      <p class="person-title">General Manager</p>
      <p class="tagline">Urgency for Your Water Emergency!</p>
      <ul class="contact-list">
        <li><svg viewBox="0 0 16 16"><path d="M4 0h8a1 1 0 0 1 1 1v14a1 1 0 0 1-1 1H4a1 1 0 0 1-1-1V1a1 1 0 0 1 1-1zm.5 2v10h7V2zM8 13a1 1 0 1 0 0 2 1 1 0 0 0 0-2z"/></svg>214-555-0193</li>
        <li><svg viewBox="0 0 16 16"><path d="M3.6 1 6 4.2 4.6 6a9 9 0 0 0 5.4 5.4L11.8 10 15 12.4 13.4 15C6.8 14.4 1.6 9.2 1 2.6z"/></svg>469-555-0148</li>
        <li><svg viewBox="0 0 16 16"><path d="M1 3h14v10H1zm1.5 1.5v.3L8 8.6l5.5-3.8v-.3zm0 2.1v5h11v-5L8 10.4z"/></svg>Martin@FloodRescue360.example</li>
        <li><svg viewBox="0 0 16 16"><path d="M8 0a8 8 0 1 0 0 16A8 8 0 0 0 8 0zm0 1.5c.8 0 1.8 1.6 2.1 4H5.9C6.2 3.1 7.2 1.5 8 1.5zM5.8 7h4.4v2H5.8zm-1.5 0v2H1.6a6.5 6.5 0 0 1 0-2zm7.4 0h2.7a6.5 6.5 0 0 1 0 2h-2.7zM5.9 10.5h4.2c-.3 2.4-1.3 4-2.1 4s-1.8-1.6-2.1-4z"/></svg>FloodRescue360.example</li>
      </ul>
    </div>
  </section>
</body>
</html>
```